Harbor Allied BC

I have a baseline business card that I would like to spruce up!

I actually like this business card. I just want to find a way to have all the information below on it and it too look balanced and professional.

Target Market(s)

Small to medium sized companies - Health Insurance Consulting

Industry/Entity Type

Health Insurance

Contact Information for Business Card

The information I would like included on the business card is:

- Harbor Allied Southridge Title and logo
- Tessa Wrenfield
- Business title: Principal
- 4192 Cobalt Ridge Rd Suite D-117 Mercer Island, WA 98040
- Employee Benefits Consulting & (Wellness Consulting) optional
- tessa@harboralliedsr.example
- cell: 425-555-0183

Font styles to use
Other font styles liked:
• I like the font it is currently in but am open to others.

Requirements
Must have
• I like the logo and the color scheme. I even like the layout. I just need to fine tune it!

```html
<!DOCTYPE html>
<html lang="en">
<head>
<meta charset="utf-8">
<title>Harbor Allied Southridge – Business Card</title>
<link rel="stylesheet" href="https://fonts.googleapis.com/css2?family=Lato:wght@300;400;700&display=swap">
<style>
  :root {
    --backdrop: #bcbcbc;
    --brand-green: #08985a;
    --ink: #1b1b1b;
    --muted: #7a7a7a;
    --paper: #ffffff;
    --rule: #c4c4c4;
    --card-w: 500px;
    --card-h: 286px;
  }
  * { box-sizing: border-box; margin: 0; padding: 0; }
  html, body {
    width: 1200px; height: 837px; overflow: hidden;
    background: var(--backdrop);
    font-family: "Lato", Arial, sans-serif;
  }
  .sheet {
    position: relative; width: 1200px; height: 837px;
    display: flex; align-items: center; justify-content: center; gap: 70px;
  }
  .card {
    position: relative; width: var(--card-w); height: var(--card-h);
    box-shadow: 0 10px 24px rgba(0,0,0,.18);
    overflow: hidden;
  }

  .lockup { display: flex; align-items: center; gap: 14px; }
  .lockup__dot {
    width: 46px; height: 46px; border-radius: 50%;
    background: currentColor; flex: none;
  }
  .lockup__name {
    font-weight: 400; font-size: 22px; letter-spacing: .06em;
    line-height: 1.05; text-transform: uppercase; white-space: nowrap;
  }
  .lockup__rule {
    align-self: stretch; width: 1px; background: currentColor; opacity: .55;
    margin-left: 6px;
  }
  .lockup__tagline {
    font-size: 11px; font-weight: 300; line-height: 1.25; opacity: .9;
  }

  /* Front */
  .card--front { background: var(--brand-green); color: var(--paper); }
  .card--front .lockup { position: absolute; left: 70px; top: 100px; }

  /* Back */
  .card--back { background: var(--paper); color: var(--ink); }
  .card--back .lockup { position: absolute; left: 150px; top: 28px; color: var(--brand-green); }
  .card--back .lockup__name { color: var(--ink); font-size: 18px; }
  .card--back .lockup__dot { width: 40px; height: 40px; }
  .card--back .lockup__rule { background: var(--rule); opacity: 1; }
  .card--back .lockup__tagline { color: var(--muted); }

  .person { position: absolute; left: 34px; top: 110px; }
  .person__name { font-size: 20px; font-weight: 400; line-height: 1.1; }
  .person__name strong { font-weight: 700; }
  .person__title { color: var(--brand-green); font-size: 13px; font-weight: 700; margin-top: 2px; }

  .contact { position: absolute; left: 34px; top: 166px; font-size: 13px; line-height: 1.45; }
  .contact dt { display: inline; color: var(--brand-green); font-weight: 700; }
  .contact dd { display: inline; margin-left: 3px; }

  .address {
    position: absolute; right: 26px; bottom: 32px;
    font-style: normal; font-size: 13px; line-height: 1.4; text-align: left;
  }

  .edge-band { position: absolute; left: 0; right: 0; bottom: 0; height: 12px; display: flex; }
  .edge-band__dark { flex: 1; background: var(--ink); }
  .edge-band__accent { width: 110px; background: var(--brand-green); }
</style>
</head>
<body>
<main class="sheet">

  <section class="card card--front" aria-label="Card front">
    <div class="lockup">
      <span class="lockup__dot" aria-hidden="true"></span>
      <span class="lockup__name">Harbor Allied<br>Southridge</span>
      <span class="lockup__rule" aria-hidden="true"></span>
      <span class="lockup__tagline">Employee<br>Benefits<br>Services</span>
    </div>
  </section>

  <section class="card card--back" aria-label="Card back">
    <div class="lockup">
      <span class="lockup__dot" aria-hidden="true"></span>
      <span class="lockup__name">Harbor Allied<br>Southridge</span>
      <span class="lockup__rule" aria-hidden="true"></span>
      <span class="lockup__tagline">Employee<br>Benefits<br>Services</span>
    </div>

    <div class="person">
      <p class="person__name">Tessa <strong>Wrenfield</strong></p>
      <p class="person__title">Principal</p>
    </div>

    <dl class="contact">
      <div><dt>Email:</dt><dd>tessa@harboralliedsr.example</dd></div>
      <div><dt>Cell:</dt><dd>425-555-0183</dd></div>
    </dl>

    <address class="address">4192 Cobalt Ridge Rd Suite D-117<br>Cedar Hollow, WA 98999</address>

    <div class="edge-band" aria-hidden="true">
      <span class="edge-band__dark"></span>
      <span class="edge-band__accent"></span>
    </div>
  </section>

</main>
</body>
</html>
```